Silver Orchard Brochure

I would like to design an e-brochure to be sent to a particular fashion designer that we choose to invite to be featured on our platform. The brochure should reflect the existing brand image of the website. The brochure will probably have no more than four to five pages and will include the following information

1) Cover Page

2) About Us

3) Our Unique Edge

4) Member Benefits

5) Prices

6) Contact

hello designers think some people are confused about what the brochure is about i have uploaded a file with the sample text - hope this helps

Reason: Hi everyone I have extended the deadline as i have uploaded a text document for the brochure that should assist with thinking about the design. please email if you have questions

Hi I have got feedback that the document wasn't uploaded properly - the sample text to work with is now uploaded on docx format Thanks

Target Market(s)

Fashion designers

Industry/Entity Type

Fashion

Requirements
Must have
• Must be cool, edgy , contemporary and inviting

please see website www.silverorchardlane.com - as look and feel should tie in with that

photos and art work can be used from website and all our social media pages

```html
<!DOCTYPE html>
<html lang="en">
<head>
<meta charset="utf-8">
<title>Silver Orchard – Member Benefits &amp; Prices</title>
<link rel="stylesheet" href="https://fonts.googleapis.com/css2?family=Roboto:wght@400;700&family=Roboto+Condensed:wght@400;700&display=swap">
<style>
  :root {
    --backdrop: #8c8c8c;
    --paper: #ffffff;
    --paper-shade: #f1f1f1;
    --ink: #1a1a1a;
    --label-bg: #141414;
    --label-text: #ffffff;
    --rule: #2a2a2a;
    --model-one: #d9d2cf;
    --model-one-deep: #6a3a5c;
    --shopfront-a: #c9c23a;
    --shopfront-b: #3f4a40;
    --model-three: #2b2a3a;
    --park-light: #e8e6dc;
    --park-mid: #8fa05a;
    --park-ground: #6b5a47;
  }
  * { box-sizing: border-box; margin: 0; padding: 0; }
  html, body {
    width: 1200px; height: 800px; overflow: hidden;
    background: var(--backdrop);
  }
  .spread {
    position: absolute; left: 120px; top: 60px;
    width: 960px; height: 680px;
    display: flex;
  }
  .page { position: relative; width: 480px; height: 680px; }
  .page--info {
    background: linear-gradient(to right, var(--paper) 85%, var(--paper-shade));
    font-family: "Roboto Condensed", Arial, sans-serif;
    color: var(--ink);
  }
  .section-head {
    position: absolute; left: 28px; right: 22px;
    display: flex; align-items: flex-end;
  }
  .section-head__label {
    background: var(--label-bg); color: var(--label-text);
    font-family: "Roboto", Arial, sans-serif; font-weight: 400;
    font-size: 14px; letter-spacing: 3px;
    padding: 7px 18px 6px 14px; white-space: nowrap;
  }
  .section-head__rule { flex: 1; height: 1px; background: var(--rule); }
  .benefits-head { top: 26px; }
  .prices-head { top: 286px; }

  .photo { position: absolute; }
  .photo--model-one {
    left: 72px; top: 72px; width: 78px; height: 190px;
    background: linear-gradient(to bottom, var(--paper) 0 8%, var(--model-one) 30%, var(--model-one-deep) 60%, var(--model-one) 85%, var(--paper));
    border-radius: 30px 30px 6px 6px;
  }
  .photo--shopfront {
    left: 28px; top: 326px; width: 164px; height: 200px;
    background: linear-gradient(110deg, var(--shopfront-b) 0 20%, var(--shopfront-a) 40%, #e7e4d8 60%, var(--shopfront-b));
  }
  .photo--model-three {
    left: 78px; top: 536px; width: 76px; height: 130px;
    background: linear-gradient(to bottom, var(--paper) 0 6%, var(--model-three) 25%, #4a3a55 70%, #b9b3b8);
    border-radius: 28px 28px 4px 4px;
  }

  .copy { position: absolute; font-size: 10.5px; line-height: 1.3; }
  .copy p { margin-bottom: 9px; }
  .benefits-copy { left: 200px; top: 74px; width: 225px; }
  .prices-copy { left: 204px; top: 326px; width: 256px; font-size: 10px; line-height: 1.25; }
  .prices-copy p { margin-bottom: 8px; }
  .package-name { font-weight: 700; display: block; }
  .lead-in { font-weight: 700; }

  .page--photo {
    background: linear-gradient(to bottom, var(--park-light) 0 40%, var(--park-mid) 58%, var(--park-ground) 80%, #b5a994);
  }
</style>
</head>
<body>
  <main class="spread">
    <section class="page page--info">
      <header class="section-head benefits-head">
        <h2 class="section-head__label">MEMBER BENEFITS</h2>
        <span class="section-head__rule"></span>
      </header>
      <div class="photo photo--model-one" role="img" aria-label="Model in a white and purple striped wrap jacket"></div>
      <div class="copy benefits-copy">
        <p>Free UK express tracked and signed delivery on all orders.</p>
        <p>Free international tracked and signed delivery on all orders over £100.</p>
        <p>£10.00 for delivery of international orders under £100.</p>
        <p>28 day returns.</p>
        <p>We accept Pursewick, Velmora (Credit and Debit), Tallycrest (Credit and Debit) and Harbourline Express.</p>
      </div>

      <header class="section-head prices-head">
        <h2 class="section-head__label">MEMBER PRICES</h2>
        <span class="section-head__rule"></span>
      </header>
      <div class="photo photo--shopfront" role="img" aria-label="Model standing beside a boutique shop window"></div>
      <div class="copy prices-copy">
        <p><span class="package-name">Entry Package</span>Online Sales Only £99 per month and 10% on each sale</p>
        <p><span class="package-name">Premium Package</span>Online Sales, Events and Blog features £199 per month and no commision charged on sales. When an item is sold at a live event we take just £50 off the first sale to cover our cost. Everything else and all additional PR etc is free and you keep all the rest of the money from what you sell.</p>
        <p><span class="package-name">VIP Package</span>All of the above plus features in our blog £250 per month and no other costs to pay ever.</p>
        <p><span class="package-name">Early Bird Offer</span>Plus at the moment we have an exclusive early bird offer if you pay upfront for the year you save £388 and only pay £2000 per annum.</p>
        <p><span class="lead-in">Think about it</span> - for most of you that means you will cover your cost if you just make a few sales a year! Not to mention the fact that we are providing exposure pr and getting your brand out there too! We doubt you will not need another PR outlet as we will work so hard for you!</p>
      </div>
      <div class="photo photo--model-three" role="img" aria-label="Model in a dark jacket with a sheer overskirt"></div>
    </section>

    <section class="page page--photo" role="img" aria-label="Model in a navy velvet dress standing under a tree in a park"></section>
  </main>
</body>
</html>
```